Business Card - Professional Minimalist - Double sided

We appreciate minimalist logo/web/collateral designs that allow design to tell a story. We want to relay a professional image/approach but throwing in a splash of modern when we’re able so long as it’s not distracting. Think 75% classic corporate, 25% modern. Open to black or white design, not sure which might look the best.

Target Market(s)

Senior executives or related government affairs contacts within the agriculture, energy, and defense industries (i.e., potential clients) but located outside of Washington, DC. Most potential clients based in DC with be familiar with both of us and our shared history.

Industry/Entity Type

Consulting

Contact Information for Business Card

Name: Daniel R. Whitlock
Title: Co-Founder & Partner
Address: 418 Bramblewood Ave. SE | Suite 2716 | Washington, D.C. 20019
Phone: (202) 555-0187
Email: Daniel@HollerbyWhitlock.com

Font styles to use
Serif

Colors

Designer to choose only greyscale colors for use in the design.

Requirements
Must have
• Name: Daniel R. Whitlock
Phone: (202) 555-0187

```html
<!DOCTYPE html>
<html lang="en">
<head>
<meta charset="utf-8">
<title>Hollerby Whitlock Group — Business Card</title>
<link rel="stylesheet" href="https://fonts.googleapis.com/css2?family=Marcellus&display=swap">
<style>
  :root {
    --page-bg: #e9e9e9;
    --card-bg: #ffffff;
    --ink-dark: #4a4a4a;
    --ink-mid: #5e5e5e;
    --ink-light: #9a9a9a;
    --pattern-top: #e4e4e4;
    --pattern-fade: #ffffff;
    --card-shadow: rgba(0, 0, 0, 0.18);
  }
  * { box-sizing: border-box; margin: 0; padding: 0; }
  html, body {
    width: 1200px;
    height: 1200px;
    overflow: hidden;
    background: var(--page-bg);
    font-family: "Marcellus", serif;
  }
  .canvas {
    position: relative;
    width: 1200px;
    height: 1200px;
  }
  .card {
    position: absolute;
    left: 170px;
    width: 860px;
    height: 491px;
    background: var(--card-bg);
    box-shadow: 0 6px 18px var(--card-shadow);
    overflow: hidden;
  }
  .card--front { top: 70px; }
  .card--back { top: 640px; }

  /* Front side */
  .front-texture {
    position: absolute;
    inset: 0;
    background: linear-gradient(170deg, var(--pattern-top) 0%, #f1f1f1 35%, var(--pattern-fade) 80%);
  }
  .front-wordmark {
    position: absolute;
    left: 0;
    right: 0;
    top: 300px;
    display: flex;
    justify-content: center;
    align-items: center;
    gap: 18px;
  }

  /* Wordmark */
  .wordmark-square {
    width: 44px;
    height: 44px;
    background: var(--ink-dark);
    flex: none;
  }
  .wordmark-name {
    font-size: 38px;
    letter-spacing: 1.5px;
    color: var(--ink-dark);
    text-transform: uppercase;
    white-space: nowrap;
  }

  /* Back side */
  .back-wordmark {
    position: absolute;
    left: 0;
    right: 0;
    top: 110px;
    display: flex;
    justify-content: center;
    align-items: center;
    gap: 18px;
  }
  .holder {
    position: absolute;
    left: 70px;
    bottom: 72px;
  }
  .holder-name {
    font-size: 31px;
    color: var(--ink-dark);
    line-height: 1.1;
  }
  .holder-title {
    font-size: 21px;
    color: var(--ink-mid);
    letter-spacing: 0.5px;
    margin-top: 4px;
  }
  .contact {
    position: absolute;
    right: 50px;
    bottom: 72px;
    list-style: none;
    text-align: right;
    color: var(--ink-dark);
    font-size: 18px;
    line-height: 1.3;
  }
  .contact-item {
    display: flex;
    justify-content: flex-end;
    align-items: flex-start;
    gap: 12px;
    margin-top: 14px;
  }
  .contact-icon {
    width: 22px;
    height: 22px;
    flex: none;
    margin-top: 1px;
  }
  .contact-icon path,
  .contact-icon circle,
  .contact-icon rect { stroke: var(--ink-light); fill: none; stroke-width: 2; }
</style>
</head>
<body>
<main class="canvas">

  <section class="card card--front" aria-label="Card front">
    <div class="front-texture" role="img" aria-label="Faint repeating monogram pattern in light grey, fading toward the bottom"></div>
    <div class="front-wordmark">
      <span class="wordmark-square"></span>
      <span class="wordmark-name">Hollerby Whitlock Group</span>
    </div>
  </section>

  <section class="card card--back" aria-label="Card back">
    <div class="back-wordmark">
      <span class="wordmark-square"></span>
      <span class="wordmark-name">Hollerby Whitlock Group</span>
    </div>

    <div class="holder">
      <p class="holder-name">Daniel R. Whitlock</p>
      <p class="holder-title">Co-Founder &amp; Partner</p>
    </div>

    <ul class="contact">
      <li class="contact-item">
        <span>418 Bramblewood Ave. SE | Suite 2716<br>Washington, D.C. 20019</span>
        <svg class="contact-icon" viewBox="0 0 24 24" aria-hidden="true">
          <path d="M12 22s-7-7.5-7-12.5a7 7 0 0 1 14 0C19 14.5 12 22 12 22z"/>
          <circle cx="12" cy="9.5" r="2.5"/>
        </svg>
      </li>
      <li class="contact-item">
        <span>(202) 555-0187</span>
        <svg class="contact-icon" viewBox="0 0 24 24" aria-hidden="true">
          <path d="M5 3h4l2 5-2.5 1.5a11 11 0 0 0 6 6L16 13l5 2v4a2 2 0 0 1-2 2A17 17 0 0 1 3 5a2 2 0 0 1 2-2z"/>
        </svg>
      </li>
      <li class="contact-item">
        <span>daniel@hollerbywhitlock.com</span>
        <svg class="contact-icon" viewBox="0 0 24 24" aria-hidden="true">
          <rect x="2" y="5" width="20" height="14"/>
          <path d="M2 5l10 8 10-8"/>
        </svg>
      </li>
    </ul>
  </section>

</main>
</body>
</html>
```